Business Image

I have recently had a new company logo made up and require some new business cards to go with it.

Target Market(s)

Developers & high worth clients.

Industry/Entity Type

Business

Contact Information for Business Card

The business is in the construction/management industry. It needs to be classy but have a industrial feel. I would like the business card to be a elegant presentation in itself.

Requirements
Must have
• Current logo & company name. Colouring needs to be the same as the current design also.
Nice to have
• A few different designs & presentations of single and double sided business cards.

```html
<!DOCTYPE html>
<html lang="en">
<head>
<meta charset="utf-8">
<title>Forgeline Build Group – Business Cards</title>
<link href="https://fonts.googleapis.com/css2?family=Tinos:wght@700&family=Open+Sans:wght@400;600&display=swap" rel="stylesheet">
<style>
  :root {
    --bg: #dcdcdc;
    --card: #ffffff;
    --blue: #5b86c8;
    --dark: #38383a;
    --dark-deep: #2c2c2e;
    --ink: #2a2a2a;
    --light-text: #f2f2f2;
  }
  * { box-sizing: border-box; margin: 0; padding: 0; }
  html, body { width: 1200px; height: 1000px; overflow: hidden; }
  body {
    background: var(--bg);
    font-family: "Open Sans", Arial, sans-serif;
    position: relative;
  }
  .card {
    position: absolute;
    width: 640px;
    height: 366px;
    background: var(--card);
    box-shadow: 0 6px 18px rgba(0,0,0,0.18);
    overflow: hidden;
  }
  /* back side */
  .card-back { left: 90px; top: 120px; }
  .card-back .edge-stripe {
    position: absolute; left: 0; top: 0; bottom: 0; width: 10px;
    background: var(--blue);
  }
  .card-back .brand { position: absolute; left: 0; right: 0; top: 112px; }
  .card-back .email {
    position: absolute; left: 34px; bottom: 28px;
    font-size: 15px; color: var(--ink);
  }
  /* front side */
  .card-front { left: 480px; top: 500px; display: flex; }
  .card-front .edge-stripe-left { width: 14px; background: var(--blue); }
  .card-front .edge-stripe-right { width: 8px; background: var(--blue); }
  .contact-panel {
    width: 300px;
    background: linear-gradient(135deg, var(--dark), var(--dark-deep));
    padding: 76px 0 0 26px;
    display: flex; flex-direction: column; gap: 30px;
  }
  .contact-row {
    display: flex; align-items: flex-start; gap: 20px;
    color: var(--light-text); font-size: 13.5px; line-height: 1.4;
  }
  .contact-row svg { flex: none; width: 24px; height: 24px; margin-top: -2px; }
  .brand-panel { flex: 1; display: flex; align-items: center; justify-content: center; }
  .brand { display: flex; flex-direction: column; align-items: center; gap: 18px; }
  .brand-mark { width: 92px; height: 92px; background: var(--blue); }
  .brand-name {
    font-family: "Tinos", "Times New Roman", serif;
    font-weight: 700; color: var(--blue);
    font-size: 30px; line-height: 1.05; text-align: center; letter-spacing: 0.5px;
  }
</style>
</head>
<body>

<section class="card card-back" aria-label="Business card, back side">
  <div class="edge-stripe"></div>
  <div class="brand">
    <div class="brand-mark"></div>
    <div class="brand-name">FORGELINE<br>BUILD GROUP</div>
  </div>
  <p class="email">daniel@forgelinebuild.com</p>
</section>

<section class="card card-front" aria-label="Business card, front side">
  <div class="edge-stripe-left"></div>
  <div class="contact-panel">
    <div class="contact-row">
      <svg viewBox="0 0 24 24"><circle cx="12" cy="12" r="12" fill="#5b86c8"/><rect x="8.5" y="5.5" width="7" height="13" rx="1.2" fill="none" stroke="#fff" stroke-width="1.4"/><circle cx="12" cy="16.3" r="0.8" fill="#fff"/></svg>
      <span>1 (555) 014-2201</span>
    </div>
    <div class="contact-row">
      <svg viewBox="0 0 24 24"><circle cx="12" cy="12" r="12" fill="#5b86c8"/><path d="M8 6.5l2 0 1 3-1.4 1.1a8 8 0 0 0 3.8 3.8L14.5 13l3 1v2a1.5 1.5 0 0 1-1.6 1.5A10 10 0 0 1 6.5 8.1 1.5 1.5 0 0 1 8 6.5z" fill="#fff"/></svg>
      <span>1 (555) 014-2277</span>
    </div>
    <div class="contact-row">
      <svg viewBox="0 0 24 24"><circle cx="12" cy="12" r="12" fill="#5b86c8"/><path d="M12 5.5a4.5 4.5 0 0 0-4.5 4.5c0 3.4 4.5 8.5 4.5 8.5s4.5-5.1 4.5-8.5A4.5 4.5 0 0 0 12 5.5z" fill="#fff"/><circle cx="12" cy="10" r="1.7" fill="#5b86c8"/></svg>
      <span>48 Harbor Row, Millbrook, NY 10990<br>, USA</span>
    </div>
    <div class="contact-row">
      <svg viewBox="0 0 24 24"><circle cx="12" cy="12" r="12" fill="#5b86c8"/><rect x="6" y="7.5" width="12" height="9" rx="1" fill="#fff"/><path d="M6.5 8l5.5 4.5L17.5 8" fill="none" stroke="#5b86c8" stroke-width="1.4"/></svg>
      <span>daniel@forgelinebuild.com</span>
    </div>
  </div>
  <div class="brand-panel">
    <div class="brand">
      <div class="brand-mark"></div>
      <div class="brand-name">FORGELINE<br>BUILD GROUP</div>
    </div>
  </div>
  <div class="edge-stripe-right"></div>
</section>

</body>
</html>
```